Business Card Design Project

I own a dental practice and would like to use a logo that was recently designed to make business cards.
I am looking for a clean card with the following information on the card.

Halvorsen Dental Center (Using the logo)
Martin L. Halvorsen, D.D.S.
7234 Pinewick Ave. Suite B
Colorado Springs, CO 80547
(719) 482-6130
halvorsendentalcenter@mailbox-example.net
www.halvorsendentalcenter.example

Also a list of items on the back:
Services include

Family Dentistry
Cosmetic
Whitening
Tooth Colored Fillings
Crowns/Bridges
Implants/Tooth Replacement
Dentures
Root Canals
Updates

Just an FYI, I added an email address and website address.

I also added my Pic.  Please give designs with and without the pic

Thanks

Target Market(s)

20-70 U.S. Female that handles the household budget.

Industry/Entity Type

Dental

Requirements
Must have
• The logo is key. The color scheme of the logo is also key. The back of the business card should have the list of Dental Services offered at the practice. The front should be clean and professional looking. No cartoons. I will also include a picture of myself. I think that the final card may or may not include this picture, so the card designs should come with and without the picture. USE THE BLUE LOGO ONLY!!!
Should not have
• NO teeth should be on the card.

```html
<!DOCTYPE html>
<html lang="en">
<head>
<meta charset="utf-8">
<title>Halvorsen Dental Center – Business Card</title>
<link rel="stylesheet" href="https://fonts.googleapis.com/css2?family=Didact+Gothic&family=Questrial&display=swap">
<style>
  :root {
    --backdrop: #e9eaee;
    --card-white: #fbfcfc;
    --slate-dark: #46636f;
    --slate-light: #7d98a4;
    --band-blue: #6890a2;
    --accent-blue: #5f8ea3;
    --ink-brown: #564845;
    --ink-grey: #6f6a69;
    --list-ink: #eef3f5;
  }
  * { margin: 0; padding: 0; box-sizing: border-box; }
  html, body {
    width: 1200px; height: 934px; overflow: hidden;
    background: var(--backdrop);
    font-family: "Didact Gothic", "Questrial", sans-serif;
  }
  .sheet {
    position: relative; width: 1200px; height: 934px;
    display: flex; align-items: center; justify-content: center; gap: 40px;
  }
  .card {
    position: relative; width: 540px; height: 309px; overflow: hidden;
    box-shadow: 0 6px 18px rgba(60, 70, 80, 0.18);
  }
  /* Back side */
  .card-back {
    background: linear-gradient(160deg, var(--slate-dark) 0%, #5a7884 55%, var(--slate-light) 100%);
  }
  .card-back .band {
    position: absolute; left: 0; right: 0; bottom: 0; height: 26px;
    background: rgba(255, 255, 255, 0.12);
  }
  .services {
    list-style: none; position: absolute; left: 40px; top: 34px;
    color: var(--list-ink); font-size: 19px; line-height: 28px; letter-spacing: 0.3px;
  }
  .services li::before { content: "· "; }
  /* Front side */
  .card-front { background: var(--card-white); }
  .card-front .band {
    position: absolute; left: 0; right: 0; bottom: 0; height: 34px;
    background: var(--band-blue);
  }
  .brand {
    position: absolute; left: 34px; top: 40px;
    display: flex; align-items: center; gap: 14px;
  }
  .brand-dot {
    width: 34px; height: 34px; border-radius: 50%; background: var(--accent-blue);
  }
  .brand-name {
    font-family: "Questrial", sans-serif; font-size: 30px; color: var(--ink-brown);
    letter-spacing: 0.2px;
  }
  .contact-primary {
    position: absolute; right: 30px; top: 150px; text-align: right;
    font-size: 14px; color: var(--ink-grey); line-height: 20px;
  }
  .doctor { color: var(--ink-brown); font-weight: 700; letter-spacing: 0.6px; }
  .doctor .creds { font-weight: 400; letter-spacing: 0; font-size: 12px; }
  .label { color: var(--accent-blue); font-weight: 700; }
  .contact-secondary {
    position: absolute; left: 34px; bottom: 52px;
    font-size: 12.5px; color: var(--ink-grey); line-height: 19px;
  }
</style>
</head>
<body>
<main class="sheet">
  <section class="card card-back" aria-label="Back of card: services">
    <ul class="services">
      <li>Family Dentistry</li>
      <li>Cosmetic</li>
      <li>Whitening</li>
      <li>Tooth Colored Fillings</li>
      <li>Crowns/Bridges</li>
      <li>Implants/Tooth Replacement</li>
      <li>Dentures</li>
      <li>Root Canals</li>
    </ul>
    <div class="band"></div>
  </section>

  <section class="card card-front" aria-label="Front of card: contact details">
    <div class="brand">
      <span class="brand-dot"></span>
      <span class="brand-name">Halvorsen Dental Center</span>
    </div>
    <div class="contact-primary">
      <p><span class="doctor">MARTIN L. HALVORSEN<span class="creds">, D.D.S.</span></span> · <span class="label">T.</span> (719) 482-6130</p>
      <p>www.halvorsendentalcenter.example</p>
    </div>
    <div class="contact-secondary">
      <p>7234 Pinewick Ave. Suite B, Colorado Springs, CO 80547</p>
      <p><span class="label">E.</span> halvorsendentalcenter@mailbox-example.net</p>
    </div>
    <div class="band"></div>
  </section>
</main>
</body>
</html>
```